Webdesign for an Health & Beauty Center

We need a new modern and elegant web design for the relaunch of the http://veskarin.at/ website.
The website is for a company which offer all services for a beuty center like epilation, cosmetics and more.
The new website should use big emotional background images and a modern menu.
All in all the website should give a female expression and the design should be clear and not playful.
The existing logo used be used for the new design, the base colours of the existing website could be used optionally.

Reason: Review of the designs together with the customer needs a little more time.

Industry/Entity Type
It Company
Look and feel
Each slider illustrates characteristics of the customer's brand and the style your logo design should communicate.

```html
<!DOCTYPE html>
<html lang="en">
<head>
<meta charset="utf-8">
<title>Veskarin Health &amp; Beauty Center</title>
<link rel="stylesheet" href="https://fonts.googleapis.com/css2?family=Arimo:ital,wght@0,400;0,700;1,400&family=Open+Sans:wght@600&display=swap">
<style>
:root{
  --nav-top:#5cc12a;
  --nav-bottom:#2f8a14;
  --brown:#7a3500;
  --green:#22ad2a;
  --orange:#ff8c0a;
  --white:#ffffff;
  --panel:rgba(255,255,255,0.72);
  --bg-light:#d9d8d6;
  --bg-mid:#a9a6a3;
  --bg-dark:#1c1817;
  --search:#e4f1df;
  --logo:#b9a793;
}
*{margin:0;padding:0;box-sizing:border-box}
html,body{width:1200px;height:1000px;overflow:hidden}
body{font-family:'Arimo',Arial,sans-serif;position:relative;background:var(--bg-dark)}
.backdrop{position:absolute;inset:0;background:
  radial-gradient(ellipse 260px 500px at 1150px 620px,rgba(40,35,33,.85),transparent 70%),
  linear-gradient(180deg,var(--bg-light) 0%,#e6e5e3 30%,#c8c6c3 60%,var(--bg-mid) 72%,#4d4544 82%,var(--bg-dark) 100%)}
.topbar{position:absolute;left:0;top:0;width:1200px;height:41px;background:linear-gradient(180deg,var(--nav-top),var(--nav-bottom))}
.main-nav a{position:absolute;top:4px;height:33px;color:var(--white);text-decoration:none;font-size:14px;line-height:38px}
.main-nav .sep{position:absolute;top:4px;width:1px;height:33px;background:rgba(255,255,255,.75)}
.main-nav .current{color:#111}
.search{position:absolute;left:870px;top:6px;width:195px;height:28px;border-radius:14px;background:var(--search)}
.search-icon{position:absolute;left:1068px;top:4px}
.headline{position:absolute;left:0;width:1186px;top:50px;text-align:center;color:var(--brown);font-size:70px;font-weight:400;letter-spacing:1px}
.save{position:absolute;left:50px;top:160px;font-size:73px}
.save b{color:var(--green)}
.save i{color:var(--orange)}
.brand{position:absolute;left:470px;top:150px;display:flex;align-items:center;gap:10px;color:var(--logo);font-size:58px;letter-spacing:4px}
.brand .dot{width:22px;height:22px;border-radius:50%;background:var(--logo)}
.promo{position:absolute;left:58px;top:280px;width:240px;height:480px;background:var(--white);box-shadow:4px 4px 4px rgba(0,0,0,.45)}
.promo-photo{position:absolute;left:9px;top:10px;width:221px;height:460px;background:linear-gradient(180deg,#8a4a1e 0%,#b0642c 40%,#c77a3a 65%,#e8dccb 85%,#c28a52 100%)}
.promo-text{position:absolute;left:28px;top:90px;width:190px;color:var(--white);font-family:'Open Sans',sans-serif;font-weight:600;font-size:22px;line-height:24px;letter-spacing:-1px}
.promo-text .pct{display:block;color:#ffb000;font-size:62px;line-height:62px;letter-spacing:-4px;margin-top:2px}
.promo-text .off{position:absolute;left:124px;top:107px;color:#ffd000;font-size:26px;line-height:26px;transform:rotate(-90deg);transform-origin:left top}
.promo-text .on{color:#ffa000;display:block}
.panel{position:absolute;background:var(--panel);border-radius:20px}
.featured{left:319px;top:288px;width:469px;height:472px}
.featured h2{position:absolute;top:10px;width:100%;text-align:center;color:var(--brown);font-size:24px}
.product{position:absolute;width:224px;text-align:center}
.product-photo{margin:0 auto;width:104px;height:132px;border-radius:14px;background:radial-gradient(ellipse 60px 70px at 50% 60%,#f3a274,#e4c7b6 70%,#ddd6d1)}
.quick-view{position:absolute;left:73px;top:60px;width:78px;height:26px;background:#ececec;border:1px solid #fff;color:#777;font-size:11px;line-height:24px;font-weight:700}
.product h3{color:var(--brown);font-size:18px;margin-top:16px;line-height:18px}
.product p{color:var(--brown);font-size:14px;line-height:14px}
.categories{left:832px;top:288px;width:267px;height:472px}
.categories h2{position:absolute;left:46px;top:16px;color:var(--brown);font-size:24px}
.categories ul{position:absolute;left:46px;top:83px;list-style:none}
.categories li{color:var(--brown);font-size:18px;line-height:31px}
.footer-col{position:absolute;top:826px;color:var(--white);font-size:14px}
.footer-col h4{font-size:14px;margin-bottom:28px}
.footer-col li{list-style:none;line-height:24px}
</style>
</head>
<body>
<div class="backdrop" role="img" aria-label="Large soft photograph of a woman's face fading into a beach with a man standing at the shore"></div>

<header class="topbar">
  <nav class="main-nav">
    <a class="current" style="left:287px">HOME</a>
    <span class="sep" style="left:348px"></span>
    <a style="left:364px">ABOUT</a>
    <span class="sep" style="left:428px"></span>
    <a style="left:448px">SPECIALS</a>
    <span class="sep" style="left:534px"></span>
    <a style="left:551px">SITEMAP</a>
    <span class="sep" style="left:625px"></span>
    <a style="left:640px">CONTACT</a>
  </nav>
  <div class="search"></div>
  <svg class="search-icon" width="34" height="32" viewBox="0 0 34 32"><circle cx="19" cy="13" r="9" fill="none" stroke="#fff" stroke-width="3"/><line x1="12" y1="20" x2="4" y2="28" stroke="#fff" stroke-width="4" stroke-linecap="round"/></svg>
</header>

<h1 class="headline">OFFER OF THE WEEK</h1>
<div class="save"><b>SAVE</b> <i>20%</i></div>
<div class="brand"><span class="dot"></span>veskarin</div>

<aside class="promo">
  <div class="promo-photo" role="img" aria-label="Spa still life with reed diffuser, towel, starfish and a white flower"></div>
  <div class="promo-text">SPECIAL<br>OFFER<span class="pct">10%</span><span class="off">OFF</span><span class="on">ON SPA<br>PRODUCTS</span></div>
</aside>

<section class="panel featured">
  <h2>FEATURED PRODUCTS</h2>
  <div class="product" style="left:0;top:58px"><div class="product-photo" role="img" aria-label="Product photo of a supplement jar"></div><div class="quick-view">quick view</div><h3>MAGNA SET</h3><p>dolor sit amet tation ullamcorper</p></div>
  <div class="product" style="left:224px;top:58px"><div class="product-photo" role="img" aria-label="Product photo of a supplement jar"></div><div class="quick-view">quick view</div><h3>MAGNA SET</h3><p>dolor sit amet tation ullamcorper</p></div>
  <div class="product" style="left:0;top:250px"><div class="product-photo" role="img" aria-label="Product photo of a supplement jar"></div><div class="quick-view">quick view</div><h3>MAGNA SET</h3><p>dolor sit amet tation ullamcorper</p></div>
  <div class="product" style="left:224px;top:250px"><div class="product-photo" role="img" aria-label="Product photo of a supplement jar"></div><div class="quick-view">quick view</div><h3>MAGNA SET</h3><p>dolor sit amet tation ullamcorper</p></div>
</section>

<section class="panel categories">
  <h2>Categories</h2>
  <ul>
    <li>Baby &amp; Child Care</li><li>Cosmetics</li><li>Diet &amp; Nutrition</li><li>Gifts &amp; Specialty</li><li>Home Medical Supplies</li><li>Household Items</li><li>Medicine Cabine</li><li>Natural Products</li><li>Online Exclusives</li><li>Sexual Health</li><li>Skin Care</li>
  </ul>
</section>

<footer>
  <div class="footer-col" style="left:170px"><h4>Information</h4><ul><li>About</li><li>Delivery</li><li>Privacy Policy</li><li>Terms &amp; Conditions</li></ul></div>
  <div class="footer-col" style="left:410px"><h4>Customer Service</h4><ul><li>Contact Us</li><li>Returns</li><li>Site Map</li></ul></div>
  <div class="footer-col" style="left:650px"><h4>Extras</h4><ul><li>Brands</li><li>Gift Vouchers</li><li>Affiliates</li><li>Specials</li></ul></div>
  <div class="footer-col" style="left:871px"><h4>My Account</h4><ul><li>My Account</li><li>Order History</li><li>Wish List</li><li>Newsletter</li></ul></div>
</footer>
</body>
</html>
```